Brightmere Business Card Redesign & Logo Update

We need to update our business cards to something more modern and fresh. Brightmere can provide the current color schemes and old design examples, but welcome creativity in helping us with this redesign. PLEASE NOTE that we no longer utilize the "tree" and/or "leaf" imagery in our branding. If able would apprecaite an update on the quality of our "words only" logo in Ai. / PNG formats too.

Target Market(s)

Investors, landowners, corporate partners, contractors

Industry/Entity Type

Environmental Restoration & Conservation

Contact Information for Business Card

Logo, persons name, title, mailing address, phone and email, website url

Font styles to use
Other font styles liked:
• Merriweather

Requirements
Nice to have
• Logo, persons name, title, mailing address, phone and email, website url, but open to ideams
Should not have
• No all back backgrounds

```html
<!DOCTYPE html>
<html lang="en">
<head>
<meta charset="utf-8">
<title>Brightmere Business Cards</title>
<link rel="stylesheet" href="https://fonts.googleapis.com/css2?family=Source+Sans+3:wght@400;600;700;800&family=Roboto+Condensed:wght@600&display=swap">
<style>
  :root {
    --bg: #e4e4e4;
    --card: #f4f4f4;
    --green: #12763c;
    --orange: #e87c22;
    --ink: #111111;
    --white: #ffffff;
  }
  * { margin: 0; padding: 0; box-sizing: border-box; }
  html, body {
    width: 1200px; height: 960px; overflow: hidden;
    background: var(--bg);
    font-family: "Source Sans 3", sans-serif;
  }
  .card {
    position: absolute; left: 295px; width: 610px; height: 349px;
    background: var(--card); border-radius: 22px; overflow: hidden;
  }
  .card--front { top: 108px; }
  .card--back { top: 510px; }
  .card__wave { position: absolute; inset: 0; width: 610px; height: 349px; }
  .brand { position: absolute; left: 0; right: 0; text-align: center; }
  .brand__name {
    display: inline-flex; align-items: center; gap: 10px;
    font-weight: 800; color: var(--green); line-height: 1; letter-spacing: 0.5px;
  }
  .brand__dot { width: 14px; height: 14px; border-radius: 50%; background: var(--orange); }
  .brand__tagline {
    font-family: "Roboto Condensed", sans-serif; font-weight: 600;
    color: var(--ink); line-height: 1;
  }
  .card--front .brand { top: 128px; }
  .card--front .brand__name { font-size: 64px; }
  .card--front .brand__tagline { font-size: 25px; margin-top: 10px; }
  .card--back .brand { top: 52px; }
  .card--back .brand__name { font-size: 56px; }
  .card--back .brand__tagline { font-size: 22px; margin-top: 8px; }
  .person {
    position: absolute; right: 324px; top: 236px; text-align: right; color: var(--white);
  }
  .person__name { font-size: 20px; font-weight: 700; line-height: 24px; }
  .person__title { font-size: 15px; line-height: 20px; margin-top: 2px; }
  .divider {
    position: absolute; left: 304px; top: 228px; width: 2px; height: 64px; background: var(--orange);
  }
  .contact { position: absolute; left: 326px; top: 228px; list-style: none; color: var(--white); }
  .contact__item { display: flex; align-items: center; gap: 5px; font-size: 15.5px; line-height: 21px; }
  .contact__icon { width: 13px; height: 13px; flex: none; }
  .address {
    position: absolute; left: 0; right: 0; top: 308px; text-align: center;
    color: var(--white); font-size: 15px;
  }
</style>
</head>
<body>
  <section class="card card--front">
    <svg class="card__wave" viewBox="0 0 610 349" aria-hidden="true">
      <path fill="var(--orange)" d="M0 299 C150 274 300 309 420 315 C520 320 585 292 610 273 V349 H0Z"/>
      <path fill="var(--green)" stroke="var(--white)" stroke-width="2" d="M0 306 C150 283 300 319 420 327 C520 333 585 302 610 278 V349 H0Z"/>
    </svg>
    <div class="brand">
      <div class="brand__name"><span>Brightmere</span><span class="brand__dot"></span></div>
      <div class="brand__tagline">Environmental Credit Company</div>
    </div>
  </section>

  <section class="card card--back">
    <svg class="card__wave" viewBox="0 0 610 349" aria-hidden="true">
      <path fill="var(--orange)" d="M0 185 C150 162 300 196 420 201 C520 205 585 178 610 157 V349 H0Z"/>
      <path fill="var(--green)" stroke="var(--white)" stroke-width="2" d="M0 192 C150 171 300 205 420 212 C520 218 585 187 610 162 V349 H0Z"/>
    </svg>
    <div class="brand">
      <div class="brand__name"><span>Brightmere</span><span class="brand__dot"></span></div>
      <div class="brand__tagline">Environmental Credit Company</div>
    </div>
    <div class="person">
      <div class="person__name">Daniel Harper</div>
      <div class="person__title">Owner</div>
    </div>
    <div class="divider"></div>
    <ul class="contact">
      <li class="contact__item">
        <svg class="contact__icon" viewBox="0 0 16 16"><path fill="none" stroke="var(--orange)" stroke-width="1.8" stroke-linejoin="round" d="M3 1.5l3 3-1.6 2a8 8 0 0 0 5.1 5.1l2-1.6 3 3-1.8 1.8C7.5 14.5 1.5 8.5 1.2 3.3Z"/></svg>
        <span>530-555-0148</span>
      </li>
      <li class="contact__item">
        <svg class="contact__icon" viewBox="0 0 16 16"><rect x="1" y="3" width="14" height="10" rx="1" fill="none" stroke="var(--orange)" stroke-width="1.8"/><path d="M1.5 3.8 8 9l6.5-5.2" fill="none" stroke="var(--orange)" stroke-width="1.6"/></svg>
        <span>daniel@brightmere.com</span>
      </li>
      <li class="contact__item">
        <svg class="contact__icon" viewBox="0 0 16 16" fill="none" stroke="var(--orange)" stroke-width="1.4"><circle cx="8" cy="8" r="6.6"/><ellipse cx="8" cy="8" rx="3" ry="6.6"/><path d="M1.4 8h13.2M2.5 4.5h11M2.5 11.5h11"/></svg>
        <span>www.brightmere.com</span>
      </li>
    </ul>
    <div class="address">418 Meadow Lane, Suite 210, Fairhaven, CA 95610</div>
  </section>
</body>
</html>
```